Harvest Smokehouse League

The current website is hslsmoke.com. We want to change the color scheme to the gold/white and black in the logo. Front page elements include everything we have except the social media links at the top can go to the bottom. We need to add fliers like http://hslsmoke.com/content/fliers/2022/SmartSelect_20211215-123241_Slides.jpg to the front page. There are more available on the events page. Also a place for a main news story on the front page. All the sponsor logos need to be present on every page. I have added a couple of more sponsor logos. On the about us page we will want to add a contact list and email form. We will take care of all functionality. You provide only design.
One site we like is tpgr.us for it is easy to navigate.
Target Market(s)
People interested in competition BBQ
Coding
Number of Pages Required
5+ page
Look and feel

```html
<!DOCTYPE html>
<html lang="en">
<head>
<meta charset="utf-8">
<title>Harvest Smokehouse League</title>
<link href="https://fonts.googleapis.com/css2?family=Gelasio:wght@400;500&family=Roboto:wght@300;400;500;700&display=swap" rel="stylesheet">
<style>
:root{
  --stage:#BC9140;
  --gold:#C49A3F;
  --gold-dark:#5a3f18;
  --ink:#070504;
  --white:#ffffff;
  --muted:#8a7a68;
  --panel:#1c1410;
  --row:#2a201a;
}
*{margin:0;padding:0;box-sizing:border-box}
html,body{width:1200px;height:3125px;overflow:hidden}
body{background:var(--stage);font-family:"Roboto",sans-serif;color:var(--white);position:relative}
.page{position:absolute;left:200px;top:406px;width:800px;height:2313px;overflow:hidden;
  background:
    radial-gradient(ellipse 420px 300px at 60px 40px,#4a2508 0%,rgba(74,37,8,0) 100%),
    radial-gradient(ellipse 500px 320px at 760px 120px,#2e1606 0%,rgba(46,22,6,0) 100%),
    linear-gradient(180deg,#1a0c04 0px,#020100 330px,#1d0f06 900px,#2a1608 1200px,#1e0f07 1600px,#120905 1800px,#221207 2100px,#0c0603 2313px);}
.abs{position:absolute}
.serif{font-family:"Gelasio",serif}
.gold{color:var(--gold)}
/* nav */
.brand{left:35px;top:20px;font-size:10.5px;font-weight:700;letter-spacing:.3px;color:var(--white);display:flex;align-items:center;gap:5px;white-space:nowrap}
.brand i{width:8px;height:8px;border-radius:50%;background:var(--gold);display:block}
.nav{left:405px;top:22px;display:flex;gap:19px;font-size:7.5px;color:#c9bba8;white-space:nowrap}
.nav .on{color:var(--gold)}
.talk{left:710px;top:15px;width:55px;height:22px;border:1px solid #c9bba8;border-radius:12px;font-size:6.5px;display:flex;align-items:center;justify-content:center}
/* hero */
.hero-place{left:97px;top:107px;font-size:8px}
.hero-title{left:97px;top:128px;font-size:42px;line-height:46px;font-weight:400;white-space:nowrap;z-index:2}
.counter{left:97px;top:251px;font-size:8px}
.thumbs{left:97px;top:271px;display:flex;gap:4px}
.thumbs span{width:25px;height:36px;background:linear-gradient(160deg,#5a4a3a,#2a2018);opacity:.6}
.thumbs span.on{background:linear-gradient(160deg,#6b4a2a,#c46a1a 60%,#3a2410);opacity:1;outline:1px solid var(--gold)}
.arrow{top:190px;width:14px;height:22px}
.flyer-back{left:510px;top:92px;width:150px;height:225px;background:var(--gold);transform:rotate(-14deg)}
.flyer{left:522px;top:100px;width:158px;height:222px;background:linear-gradient(180deg,#4a3a30 0%,#2a1e18 35%,#d9650f 65%,#f0a020 75%,#3a2418 100%);box-shadow:0 4px 14px rgba(0,0,0,.6)}
/* news */
.news{left:96px;top:381px;width:608px;height:77px;background:#2d1c0c;display:flex}
.news-body{flex:1;padding:14px 17px}
.news-body h4{font-size:7px;font-weight:500;margin-bottom:9px}
.news-items{display:flex;gap:0}
.news-items div{width:125px;font-size:6.8px;line-height:12px}
.news-items .d{color:#a8967f}
.news-items .t{color:var(--gold)}
.news-all{width:76px;background:#5a3f1a;font-size:7px;display:flex;align-items:center;justify-content:center}
/* headings */
.h2{font-size:22px;font-weight:400}
/* sponsors */
.sponsors{left:96px;top:564px;width:608px;display:grid;grid-template-columns:repeat(4,145px);gap:11px 9.5px}
.sponsor{height:101px;background:var(--white);border-bottom:4px solid var(--gold);display:flex;align-items:center;justify-content:center;gap:6px;color:#222;font-size:19px;font-weight:400;white-space:nowrap}
.sponsor i{width:18px;height:18px;border-radius:50%;background:#333;display:block}
/* team */
.team{left:96px;top:904px;width:608px;height:745px;background:linear-gradient(180deg,#201712,#1a120d);border-radius:0 0 22px 22px}
.tabs{position:absolute;left:0;top:0;width:608px;height:36px;background:#2b211b;border-radius:18px;display:flex;align-items:center;font-size:8px;font-weight:700;color:#8a7a6a}
.tabs span{flex:1;text-align:center}
.tabs .on{flex:0 0 145px;height:36px;background:var(--gold);color:var(--white);border-radius:18px;display:flex;align-items:center;justify-content:center}
.podium{position:absolute;top:94px;width:110px;text-align:center;margin-left:-55px}
.medal{width:56px;height:56px;border-radius:50%;margin:0 auto;display:flex;align-items:center;justify-content:center;font-size:30px;font-weight:700}
.pts{font-size:16px;font-weight:700;color:var(--gold);margin-top:11px}
.pname{font-size:6.5px;font-weight:700;margin-top:12px}
.pcount{font-size:6.5px;color:var(--muted);margin-top:7px}
.rows{position:absolute;left:85px;top:267px;width:438px}
.row{height:49px;background:var(--row);border-radius:16px;margin-bottom:10.5px;display:flex;align-items:center;padding:0 20px}
.row .n{width:22px;font-size:14px;color:#9a8a78;font-weight:500}
.row .nm{flex:1;font-size:8px;font-weight:700;line-height:12px}
.row .nm small{display:block;font-size:6.5px;font-weight:400;color:var(--muted)}
.row .p{font-size:8px;font-weight:700;color:var(--gold)}
.viewall{position:absolute;left:0;width:608px;top:698px;text-align:center;font-size:8px;font-weight:700;color:var(--gold)}
/* about */
.about-h{left:0;width:800px;top:1740px;text-align:center}
.about-p{left:188px;top:1789px;width:425px;text-align:center;font-size:10px;line-height:23px;font-weight:300;color:#e0d6c8}
.dots{left:165px;width:466px;border-top:1px dotted #5a4636}
/* footer */
.f-brand{left:167px;top:2019px}
.f-label{font-size:6.5px;color:#a0907c}
.f-val{font-size:7px;color:#e8e0d4}
.socials{left:167px;top:2145px;display:flex;gap:10px}
.socials i{width:8px;height:8px;border-radius:50%;background:#a0907c;display:block}
.signup{left:395px;top:2121px;width:239px;height:32px;background:var(--white);border-radius:16px;display:flex;align-items:center}
.signup span{flex:1;padding-left:18px;font-size:6.5px;color:#999}
.signup b{width:68px;height:32px;background:var(--gold);border-radius:16px;font-size:7px;font-weight:700;display:flex;align-items:center;justify-content:center;color:var(--white)}
.f-links{left:0;width:800px;top:2243px;display:flex;justify-content:center;gap:19px;font-size:7px;color:#b0a090}
</style>
</head>
<body>
<main class="page">
  <header>
    <div class="abs brand"><i></i>Harvest Smokehouse League</div>
    <nav class="abs nav"><span class="on">Home</span><span>Events</span><span>Results</span><span>About HSL</span><span>Members</span><span>Sanctioning Form</span></nav>
    <div class="abs talk">Talk to us</div>
  </header>

  <section class="hero">
    <div class="abs hero-place">Bramble, TX - <span class="gold">Jan 29</span></div>
    <div class="abs flyer-back"></div>
    <div class="abs flyer" role="img" aria-label="Event flyer for the 2022 Bramble Rodeo and BBQ Cook-Off with flames and grilled meat"></div>
    <h1 class="abs hero-title serif">Bramble Rodeo &amp;<br><span class="gold">BBQ Cook-OFF</span></h1>
    <div class="abs counter">01 / <span class="gold">04</span></div>
    <div class="abs thumbs"><span class="on"></span><span></span><span></span><span></span></div>
    <svg class="abs arrow" style="left:34px" viewBox="0 0 14 22"><path d="M11 2 L3 11 L11 20" fill="none" stroke="#8a6a3a" stroke-width="2"/></svg>
    <svg class="abs arrow" style="left:752px" viewBox="0 0 14 22"><path d="M3 2 L11 11 L3 20" fill="none" stroke="#d0b070" stroke-width="2"/></svg>
  </section>

  <section class="abs news">
    <div class="news-body">
      <h4>Recent News</h4>
      <div class="news-items">
        <div><span class="d">January 25, 2022</span><br><span class="t">TPGR January Board of Directors Meeting Canceled.</span></div>
        <div><span class="d">January 25, 2022</span><br><span class="t">NEW FOR 2022 Season</span></div>
        <div><span class="d">January 25, 2022</span><br><span class="t">TPGR Board Election – Last Call</span></div>
        <div><span class="d">January 25, 2022</span><br><span class="t">TPGR January Board of Directors Meeting Canceled.</span></div>
      </div>
    </div>
    <div class="news-all">View All</div>
  </section>

  <h2 class="abs h2 serif" style="left:96px;top:510px">Our <span class="gold">Sponsors</span></h2>
  <section class="abs sponsors">
    <div class="sponsor"><i></i>Lonestar Co</div>
    <div class="sponsor"><i></i>Ironrange</div>
    <div class="sponsor"><i></i>brightly</div>
    <div class="sponsor"><i></i>tundra</div>
    <div class="sponsor"><i></i>orbit</div>
    <div class="sponsor"><i></i>Glowmind</div>
    <div class="sponsor"><i></i>pellow</div>
    <div class="sponsor"><i></i>combly</div>
  </section>

  <h2 class="abs h2 serif" style="left:96px;top:853px">Team of the <span class="gold">Year</span></h2>
  <section class="abs team">
    <div class="tabs"><span class="on">Overall</span><span>Chicken</span><span>Ribs</span><span>Pork</span><span>Brisket</span></div>
    <div class="podium" style="left:144px"><div class="medal" style="background:#8a7c6c">2</div><div class="pts">1321 pts</div><div class="pname">Hickory Ember BBQ</div><div class="pcount">3 contests</div></div>
    <div class="podium" style="left:303px"><div class="medal" style="background:var(--gold)">1</div><div class="pts">1491 pts</div><div class="pname">Hickory Ember BBQ</div><div class="pcount">3 contests</div></div>
    <div class="podium" style="left:463px"><div class="medal" style="background:#3a2a20">3</div><div class="pts">1242 pts</div><div class="pname">Hickory Ember BBQ</div><div class="pcount">3 contests</div></div>
    <div class="rows">
      <div class="row"><span class="n">4</span><span class="nm">Hickory Ember BBQ<small>3 contests</small></span><span class="p">1321 pts</span></div>
      <div class="row"><span class="n">5</span><span class="nm">Hickory Ember BBQ<small>3 contests</small></span><span class="p">1321 pts</span></div>
      <div class="row"><span class="n">6</span><span class="nm">Hickory Ember BBQ<small>3 contests</small></span><span class="p">1321 pts</span></div>
      <div class="row"><span class="n">7</span><span class="nm">Hickory Ember BBQ<small>3 contests</small></span><span class="p">1321 pts</span></div>
      <div class="row"><span class="n">8</span><span class="nm">Hickory Ember BBQ<small>3 contests</small></span><span class="p">1321 pts</span></div>
      <div class="row"><span class="n">9</span><span class="nm">Hickory Ember BBQ<small>3 contests</small></span><span class="p">1321 pts</span></div>
      <div class="row"><span class="n">10</span><span class="nm">Hickory Ember BBQ<small>3 contests</small></span><span class="p">1321 pts</span></div>
    </div>
    <div class="viewall">View all</div>
  </section>

  <h2 class="abs h2 serif about-h">About <span class="gold">Us</span></h2>
  <p class="abs about-p">Harvest Smokehouse League is an organization founded by barbecue cooks for barbecue cooks and our main goal is to bring competition barbecue out of the stone age and into the information age… but above all we want to make barbecue fun again!</p>

  <footer>
    <div class="abs dots" style="top:1967px"></div>
    <div class="abs brand f-brand"><i></i>Harvest Smokehouse League</div>
    <div class="abs" style="left:167px;top:2053px"><div class="f-label">Call Us</div><div class="f-val" style="margin-top:6px">(555) 014-2290</div></div>
    <div class="abs" style="left:167px;top:2100px"><div class="f-label">Address</div><div class="f-val" style="margin-top:6px">1820 Mesquite Ln, Pecan Flats, TX 70000</div></div>
    <div class="abs socials"><i></i><i></i><i></i><i></i></div>
    <div class="abs" style="left:395px;top:2080px"><div class="f-label">Be Informed</div><div class="f-val" style="margin-top:7px">Get email notifications about events in your area</div></div>
    <div class="abs signup"><span>Enter your email</span><b>Subscribe</b></div>
    <div class="abs dots" style="top:2197px"></div>
    <nav class="abs f-links"><span>Home</span><span>Events</span><span>Results</span><span>About HSL</span><span>Members</span><span>Sanctioning Form</span></nav>
  </footer>
</main>
</body>
</html>
```